Zielgruppe
Folierung, Werbetechnik, Lackschutz, Beschriftung, Digitaldruck
Aufgabenstellung
Es soll ein modernes, schönes Design sein. Sind für alle vorschläge offen!
!!!!WICHTIG!!! Der Gorilla im Anhang MUSS als Logo genommen werden. !!! WICHTIG!!!
Schrift ist Porscha
Bitte beachte! Es muss KEIN neues Logo erstellt werden, sondern dass vorhandene ( Anhang,Gorilla) eingearbeitet / Intigriert werden

```html
<!DOCTYPE html>
<html lang="de">
<head>
<meta charset="utf-8">
<title>Haftkunst Brandl KR GmbH – Geschäftsausstattung</title>
<link rel="stylesheet" href="https://fonts.googleapis.com/css2?family=Michroma&family=Montserrat:wght@400;500&display=swap">
<style>
  :root {
    --teal-deep: #1f4a57;
    --teal: #245663;
    --teal-glow: #4a8a9c;
    --gold: #e9b94a;
    --gold-soft: #f2d9a3;
    --gold-pale: #f5e3bb;
    --paper: #ffffff;
    --edge: #d6d6d6;
  }
  * { box-sizing: border-box; margin: 0; padding: 0; }
  html, body { width: 1200px; height: 917px; overflow: hidden; background: var(--paper); }
  body { position: relative; font-family: "Montserrat", sans-serif; }

  .wordmark {
    font-family: "Michroma", sans-serif;
    text-transform: uppercase;
    white-space: nowrap;
    text-align: center;
    position: absolute;
    left: 0; right: 0;
  }
  .brand-dot {
    position: absolute;
    border-radius: 50%;
    background: radial-gradient(circle at 50% 40%, var(--gold-soft), var(--gold));
  }

  /* Logo on white */
  .logo-sheet { position: absolute; left: 100px; top: 90px; width: 300px; height: 170px; }
  .logo-sheet .brand-dot { left: 102px; top: 8px; width: 96px; height: 96px; opacity: .85; }
  .logo-sheet .wordmark { top: 142px; font-size: 11px; letter-spacing: 2.5px; color: var(--gold-soft); }

  /* Business cards */
  .card {
    position: absolute; left: 68px; width: 379px; height: 208px;
    background:
      radial-gradient(ellipse 42% 75% at 50% 0%, var(--teal-glow) 0%, rgba(74,138,156,0) 100%),
      var(--teal);
    overflow: hidden;
  }
  .card--front { top: 420px; }
  .card--front .brand-dot { left: 140px; top: 30px; width: 100px; height: 100px; }
  .card--front .wordmark { top: 158px; font-size: 12.5px; letter-spacing: 1.5px; color: var(--gold); }

  .card--back { top: 646px; }
  .card--back .wordmark { top: 84px; font-size: 9.5px; letter-spacing: 2.5px; color: var(--gold-soft); }
  .contact-list { position: absolute; left: 118px; top: 108px; list-style: none; }
  .contact-list li {
    display: flex; align-items: center; gap: 8px;
    height: 15.5px; font-size: 11.5px; color: var(--gold-pale);
  }
  .contact-list li.indent { padding-left: 16px; }
  .contact-list svg { width: 8px; height: 8px; fill: var(--gold-pale); flex: none; }

  /* Letterhead */
  .letterhead {
    position: absolute; left: 568px; top: 69px; width: 565px; height: 802px;
    background: var(--paper); border: 1px solid var(--edge);
  }
  .letterhead__header {
    position: absolute; left: 0; top: 0; right: 0; height: 88px;
    background:
      radial-gradient(ellipse 30% 110% at 50% 0%, var(--teal-glow) 0%, rgba(74,138,156,0) 100%),
      var(--teal);
  }
  .letterhead__header .brand-dot { left: 265px; top: 7px; width: 36px; height: 36px; }
  .letterhead__header .wordmark { top: 64px; font-size: 8.5px; letter-spacing: 1px; color: var(--gold); }

  .letterhead__footer {
    position: absolute; left: 0; right: 0; bottom: 0; height: 60px;
    background: var(--teal-deep);
    font-size: 6.6px; color: var(--gold-pale);
  }
  .footer-col { position: absolute; top: 11px; list-style: none; }
  .footer-col li { display: flex; align-items: center; gap: 4px; height: 14px; white-space: nowrap; }
  .footer-col li.indent { padding-left: 10px; }
  .footer-col svg { width: 6px; height: 6px; fill: var(--gold-pale); flex: none; }
  .footer-col--address { left: 20px; }
  .footer-col--contact { left: 151px; }
  .footer-col--bank { left: 274px; }
  .footer-col--register { left: 383px; }
</style>
</head>
<body>
<svg width="0" height="0" style="position:absolute" aria-hidden="true">
  <symbol id="icon-pin" viewBox="0 0 10 10"><path d="M5 0a3.6 3.6 0 0 0-3.6 3.6C1.4 6.3 5 10 5 10s3.6-3.7 3.6-6.4A3.6 3.6 0 0 0 5 0zm0 5a1.4 1.4 0 1 1 0-2.8A1.4 1.4 0 0 1 5 5z"/></symbol>
  <symbol id="icon-phone" viewBox="0 0 10 10"><path d="M2 .3l1.6 2.2-.9 1.1c.6 1.2 1.5 2.1 2.7 2.7l1.1-.9L8.7 7 9.7 8.3 8.4 9.6C4.3 9.6.4 5.7.4 1.6z"/></symbol>
  <symbol id="icon-mail" viewBox="0 0 10 10"><path d="M0 2h10v6H0z"/></symbol>
  <symbol id="icon-globe" viewBox="0 0 10 10"><path d="M5 0a5 5 0 1 0 0 10A5 5 0 0 0 5 0zm0 1c.5.6 1 1.7 1.1 3.5H3.9C4 2.7 4.5 1.6 5 1zM1 4.5a4 4 0 0 1 2-3c-.4.8-.7 1.8-.8 3zm0 1h1.2c.1 1.2.4 2.2.8 3a4 4 0 0 1-2-3zm2.9 0h2.2C6 7.3 5.5 8.4 5 9c-.5-.6-1-1.7-1.1-3.5zm3.9 0H9a4 4 0 0 1-2 3c.4-.8.7-1.8.8-3zm0-1c-.1-1.2-.4-2.2-.8-3a4 4 0 0 1 2 3z"/></symbol>
</svg>

<section class="logo-sheet">
  <div class="brand-dot" aria-hidden="true"></div>
  <p class="wordmark">Haftkunst Brandl KR GmbH</p>
</section>

<section class="card card--front">
  <div class="brand-dot" aria-hidden="true"></div>
  <p class="wordmark">Haftkunst Brandl KR GmbH</p>
</section>

<section class="card card--back">
  <p class="wordmark">Haftkunst Brandl KR GmbH</p>
  <ul class="contact-list">
    <li><svg><use href="#icon-pin"/></svg>Lindenweg 14</li>
    <li class="indent">78050 Musterstadt</li>
    <li><svg><use href="#icon-phone"/></svg>07721 4455120</li>
    <li><svg><use href="#icon-mail"/></svg>info@haftkunst-brandl.de</li>
    <li><svg><use href="#icon-globe"/></svg>www.haftkunst-brandl.de</li>
  </ul>
</section>

<section class="letterhead">
  <header class="letterhead__header">
    <div class="brand-dot" aria-hidden="true"></div>
    <p class="wordmark">Haftkunst Brandl KR GmbH</p>
  </header>
  <footer class="letterhead__footer">
    <ul class="footer-col footer-col--address">
      <li><svg><use href="#icon-pin"/></svg>Lindenweg 14</li>
      <li class="indent">78050 Musterstadt</li>
      <li class="indent">Inhaber Markus Feldner</li>
    </ul>
    <ul class="footer-col footer-col--contact">
      <li><svg><use href="#icon-phone"/></svg>07721 4455120</li>
      <li><svg><use href="#icon-mail"/></svg>info@haftkunst-brandl.de</li>
      <li><svg><use href="#icon-globe"/></svg>www.haftkunst-brandl.de</li>
    </ul>
    <ul class="footer-col footer-col--bank">
      <li>Bankverbindung</li>
      <li>IBAN</li>
      <li>BIC</li>
    </ul>
    <ul class="footer-col footer-col--register">
      <li>Amtsgericht: 79098 Musterburg</li>
      <li>Registernummer: HRB 512408</li>
      <li>Ust.-Id: DE291847365</li>
    </ul>
  </footer>
</section>
</body>
</html>
```